modernized upgrade to existing squarespace site

Hello! I have the following page for my consulting firm: https://hollinbrookcounsel.com/ Would love to upgrade to something more modern/attractive like here: https://www.pemberlowgroup.com/ or https://brightquillstudio.com/ , but I am open to creativity. Would like to retain the logo look and color theme from the logo. The rest can be left to creative discretion.

```html
<!DOCTYPE html>
<html lang="en">
<head>
<meta charset="utf-8">
<title>Hollinbrook Counsel</title>
<link rel="stylesheet" href="https://fonts.googleapis.com/css2?family=Baskervville&family=Poppins:wght@400;500;600&display=swap">
<style>
:root{
  --accent:#d49a8c;
  --accent-dark:#c4887a;
  --ink:#1d1d1d;
  --body:#3a3a3a;
  --muted:#6b6b6b;
  --line:#e6e6e6;
  --footer:#0b0b0b;
  --white:#ffffff;
  --serif:'Baskervville', 'Times New Roman', serif;
  --sans:'Poppins', Arial, sans-serif;
}
*{box-sizing:border-box;margin:0;padding:0}
html,body{width:1200px;height:5343px;overflow:hidden}
body{position:relative;background:var(--white);font-family:var(--sans);color:var(--body)}
.abs{position:absolute}

/* header */
.site-header{position:absolute;left:0;top:0;width:1200px;height:100px;background:var(--white)}
.brand{position:absolute;display:flex;align-items:center;gap:16px}
.brand-mark{width:64px;height:64px;border:2px solid var(--accent)}
.brand-name{font-family:var(--serif);color:var(--ink);font-size:30px;letter-spacing:4px;line-height:1}
.main-nav{position:absolute;right:66px;top:36px;display:flex;gap:22px;align-items:center;font-size:11px;color:var(--ink);font-weight:500}
.main-nav .active{border-bottom:2px solid var(--accent);padding-bottom:8px;margin-top:10px}
.nav-cta{background:var(--accent);color:var(--white);padding:8px 16px;border-radius:20px}

/* hero */
.hero{position:absolute;left:0;top:100px;width:1200px;height:708px;background:linear-gradient(120deg,#2a2a2a 0%,#4b4642 45%,#1f1d1c 100%)}
.hero-frame{position:absolute;left:272px;top:132px;width:656px;height:396px;border:2px solid rgba(255,255,255,.85);text-align:center}
.hero-frame h1{font-family:var(--serif);font-weight:400;color:var(--white);font-size:47px;line-height:60px;margin-top:58px}
.btn{display:inline-flex;align-items:center;justify-content:center;gap:10px;background:var(--accent);color:var(--white);font-family:var(--sans);font-weight:500;border-radius:32px;text-transform:uppercase}
.btn .arr{width:17px;height:17px;border-radius:50%;background:#111;display:inline-flex;align-items:center;justify-content:center}
.hero .btn{position:absolute;left:236px;top:260px;width:186px;height:60px;font-size:17px}
.hero-dots{position:absolute;left:572px;top:608px;display:flex;gap:4px}
.hero-dots span{width:11px;height:11px;border-radius:50%;background:rgba(255,255,255,.55)}
.hero-dots span:first-child{background:var(--white)}

/* section heads */
.section-head{position:absolute;display:flex;align-items:flex-start;gap:26px}
.head-mark{width:86px;height:86px;border:2px solid var(--accent);flex:none}
.section-head h2{font-family:var(--serif);font-weight:400;color:var(--ink);font-size:62px;line-height:56px;letter-spacing:1px}
.section-head p{font-family:var(--serif);color:var(--accent);font-size:38px;line-height:44px}

.lead{position:absolute;left:150px;top:1070px;width:900px;text-align:center;font-size:15px;line-height:30px;color:var(--body)}

/* cards */
.card{position:absolute;width:334px;background:var(--white);box-shadow:0 2px 12px rgba(0,0,0,.14);text-align:center}
.card .photo{position:absolute;left:8px;top:8px;width:318px;height:270px}
.card h3{position:absolute;left:0;width:100%;top:302px;font-family:var(--serif);font-weight:400;font-size:26px;color:var(--ink)}
.card .rule{position:absolute;left:147px;top:346px;width:40px;height:2px;background:var(--accent)}
.card p{position:absolute;left:22px;width:290px;top:370px;font-size:13px;line-height:25px;color:var(--body)}
.card.featured{background:var(--accent)}
.card.featured h3,.card.featured p{color:var(--white)}
.card.featured .rule{background:var(--white)}

/* split sections */
.body-copy{position:absolute;font-size:15px;line-height:30px;color:var(--body)}
.frame-line{position:absolute;border:2px solid var(--accent)}

/* testimonials */
.quote-card{position:absolute;top:3450px;width:216px;height:285px;background:var(--accent);color:var(--white);text-align:center}
.quote-card .qmark{font-family:var(--serif);font-size:80px;line-height:80px;margin-top:20px;height:60px}
.quote-card p{font-size:13px;line-height:26px;padding:14px 18px 0}
.quote-card .who{position:absolute;left:28px;top:218px;display:flex;align-items:center;gap:18px}
.avatar{width:46px;height:46px;border-radius:50%;background:#e9e2dc;border:2px solid var(--white)}
.who b{display:block;font-family:var(--serif);font-weight:400;font-size:16px}
.who i{font-style:normal;color:#f6d35a;font-size:11px;letter-spacing:1px}
.slider-arrow{position:absolute;width:40px;height:40px;border-radius:50%;display:flex;align-items:center;justify-content:center}

/* blog */
.post{position:absolute;top:4018px;width:334px;height:594px;background:var(--white);box-shadow:0 2px 12px rgba(0,0,0,.14)}
.post .photo{position:absolute;left:8px;top:8px;width:318px;height:270px}
.post blockquote{position:absolute;left:28px;top:302px;width:284px;font-family:var(--serif);font-size:24px;line-height:29px;color:var(--ink)}
.post cite{position:absolute;left:28px;top:498px;width:260px;font-style:normal;font-size:12px;line-height:24px;color:var(--accent);font-weight:500}

/* press */
.press{position:absolute;top:4846px;display:flex;align-items:center;justify-content:center;height:124px;font-family:var(--serif);color:#333}

/* footer */
.site-footer{position:absolute;left:0;top:5050px;width:1200px;height:293px;background:var(--footer);color:var(--white)}
.foot-nav{position:absolute;left:448px;top:82px;display:flex;gap:22px;font-size:12px}
.foot-nav span.sep{color:#777}
.foot-contact{position:absolute;font-size:13px;display:flex;align-items:center;gap:8px}
.ico{width:18px;height:18px;border-radius:4px;background:var(--accent);display:inline-flex;align-items:center;justify-content:center}
.foot-rule{position:absolute;left:0;top:228px;width:1200px;height:1px;background:#444}
.copyright{position:absolute;left:0;width:1200px;top:256px;text-align:center;font-size:11px}
</style>
</head>
<body>

<header class="site-header">
  <div class="brand" style="left:68px;top:18px">
    <div class="brand-mark"></div>
    <div class="brand-name">HOLLINBROOK COUNSEL</div>
  </div>
  <nav class="main-nav">
    <span class="active">HOME</span>
    <span>SERVICES ▾</span>
    <span>RESEARCH</span>
    <span>THE INSTITUTE</span>
    <span>IN THE NEWS</span>
    <span class="nav-cta">CONTACT</span>
  </nav>
</header>

<section class="hero" role="img" aria-label="Photo of hands leafing through a stack of paper reports on a desk">
  <div class="hero-frame">
    <h1>Macroeconomic &amp; policy<br>analytics for today’s<br>turbulent environment.</h1>
    <a class="btn">Contac us <span class="arr"><svg width="9" height="9" viewBox="0 0 10 10"><path d="M1 5h7M5 2l3 3-3 3" stroke="#fff" stroke-width="1.6" fill="none"/></svg></span></a>
  </div>
  <div class="hero-dots"><span></span><span></span><span></span><span></span></div>
</section>

<!-- services -->
<div class="section-head" style="left:316px;top:936px">
  <div class="head-mark"></div>
  <div><h2>OUR SERVICES</h2><p>What We Do</p></div>
</div>
<p class="lead">Our services suite focuses on providing exclusive, custom research and analytics to a select number of clients. We do so by outlining a sophisticated research plan, building teams of industry experts, and providing final analyses catered to your preferred audience.</p>

<article class="card" style="left:68px;top:1272px;height:538px">
  <div class="photo" role="img" aria-label="Laptop showing analytics charts on a desk" style="background:linear-gradient(160deg,#5a3a2a,#8fa3ad 55%,#2b2b2b)"></div>
  <h3>Analytics &amp; Messaging</h3><span class="rule"></span>
  <p>Our communications team can develop influential messaging, in conjunction with our data scientists’ technical expertise.</p>
</article>
<article class="card featured" style="left:433px;top:1212px;height:536px">
  <div class="photo" role="img" aria-label="Hands holding a rolled printed report" style="background:linear-gradient(150deg,#2c2c2c,#6a6664 60%,#3a3735)"></div>
  <h3>Customized Reports</h3><span class="rule"></span>
  <p>From succinct summations of economic and policy impact to full-length analyses, we can create the customized exposition that best represents your interests.</p>
</article>
<article class="card" style="left:798px;top:1272px;height:538px">
  <div class="photo" role="img" aria-label="Person using a laptop and phone at an outdoor table" style="background:linear-gradient(150deg,#6f9a4a,#d8d4c6 50%,#9a8f7b)"></div>
  <h3>Proprietary Surveys</h3><span class="rule"></span>
  <p>Exclusive, custom-designed surveys can enrich your databank, while maintaining access to proprietary resources, establishing you and your firm as a thought leader.</p>
</article>

<a class="btn abs" style="left:507px;top:1858px;width:186px;height:62px;font-size:17px">Contact us <span class="arr"><svg width="9" height="9" viewBox="0 0 10 10"><path d="M1 5h7M5 2l3 3-3 3" stroke="#fff" stroke-width="1.6" fill="none"/></svg></span></a>

<!-- research -->
<div class="section-head" style="left:98px;top:2058px;gap:20px">
  <div class="head-mark" style="width:80px;height:80px"></div>
  <div><h2 style="font-size:56px;line-height:52px">RESEARCH</h2><p style="font-size:34px">Research Samples</p></div>
</div>
<p class="body-copy" style="left:98px;top:2196px;width:540px">Our research spans multiple industries, with a focus on the impact of policy proposals on your company’s future.</p>
<p class="body-copy" style="left:98px;top:2286px;width:540px">Most of our work product is proprietary, but feel free to reach out for additional samples.</p>
<a class="btn abs" style="left:98px;top:2382px;width:160px;height:54px;font-size:14px">Contac us <span class="arr"><svg width="9" height="9" viewBox="0 0 10 10"><path d="M1 5h7M5 2l3 3-3 3" stroke="#fff" stroke-width="1.6" fill="none"/></svg></span></a>
<div class="frame-line" style="left:706px;top:2040px;width:396px;height:384px"></div>
<div class="abs" role="img" aria-label="City skyline with a tall skyscraper at sunset" style="left:688px;top:2056px;width:396px;height:382px;background:linear-gradient(180deg,#e9d3b8 0%,#c9a88a 45%,#5e5650 80%,#2e2c2b 100%)"></div>

<!-- institute -->
<div class="frame-line" style="left:74px;top:2573px;width:396px;height:538px"></div>
<div class="abs" role="img" aria-label="Curved aisle of library bookshelves" style="left:90px;top:2588px;width:396px;height:540px;background:linear-gradient(160deg,#0e1e3e,#2a4a7c 50%,#0b1630)"></div>
<div class="section-head" style="left:566px;top:2624px;gap:20px">
  <div class="head-mark" style="width:80px;height:80px"></div>
  <div><h2 style="font-size:56px;line-height:52px">THE INSTITUTE</h2><p style="font-size:34px">Hollinbrook Policy Institute</p></div>
</div>
<p class="abs" style="left:566px;top:2760px;width:550px;font-size:18px;line-height:34px;font-weight:600;color:var(--ink)">Thoughtful solutions that bridge the academic with private industry.</p>
<p class="body-copy" style="left:566px;top:2840px;width:560px;text-align:justify">The Hollinbrook Policy Institute (HPI) is an independent non-profit organization that partners with private think tanks, academic institutions, and policy advocacy organizations to develop unbiased investigations and reasoned responses to the macroeconomic policy concerns of today.</p>
<a class="btn abs" style="left:566px;top:3020px;width:170px;height:54px;font-size:14px">Learn more <span class="arr"><svg width="9" height="9" viewBox="0 0 10 10"><path d="M1 5h7M5 2l3 3-3 3" stroke="#fff" stroke-width="1.6" fill="none"/></svg></span></a>

<!-- testimonials -->
<div class="section-head" style="left:234px;top:3284px">
  <div class="head-mark"></div>
  <div><h2>OUR TESTIMONIALS</h2><p>What Client Says</p></div>
</div>
<div class="slider-arrow" style="left:50px;top:3572px;background:#cfcfcf"><svg width="12" height="12" viewBox="0 0 10 10"><path d="M6.5 2L3.5 5l3 3" stroke="#fff" stroke-width="1.6" fill="none"/></svg></div>
<div class="slider-arrow" style="left:1110px;top:3572px;background:#111"><svg width="12" height="12" viewBox="0 0 10 10"><path d="M3.5 2l3 3-3 3" stroke="#fff" stroke-width="1.6" fill="none"/></svg></div>

<div class="quote-card" style="left:128px"><div class="qmark">”</div><p>Lorem ipsum dolor sit amet, con sectetur adipi scing elit. Maece nas ac tellus ac ipsum porta.</p><div class="who"><span class="avatar" role="img" aria-label="Client portrait"></span><span><b>Dickens</b><i>★★★★★</i></span></div></div>
<div class="quote-card" style="left:371px"><div class="qmark">”</div><p>Lorem ipsum dolor sit amet, con sectetur adipi scing elit. Maece nas ac tellus ac ipsum porta.</p><div class="who"><span class="avatar" role="img" aria-label="Client portrait"></span><span><b>Stephen</b><i>★★★★★</i></span></div></div>
<div class="quote-card" style="left:615px"><div class="qmark">”</div><p>Lorem ipsum dolor sit amet, con sectetur adipi scing elit. Maece nas ac tellus ac ipsum porta.</p><div class="who"><span class="avatar" role="img" aria-label="Client portrait"></span><span><b>Jonathan</b><i>★★★★★</i></span></div></div>
<div class="quote-card" style="left:858px"><div class="qmark">”</div><p>Lorem ipsum dolor sit amet, con sectetur adipi scing elit. Maece nas ac tellus ac ipsum porta.</p><div class="who"><span class="avatar" role="img" aria-label="Client portrait"></span><span><b>Smith</b><i>★★★★★</i></span></div></div>

<!-- blog -->
<div class="section-head" style="left:386px;top:3862px">
  <div class="head-mark"></div>
  <div><h2>OUR BLOG</h2><p>News</p></div>
</div>
<article class="post" style="left:68px">
  <div class="photo" role="img" aria-label="Laboratory workers in protective gear with a tablet" style="background:linear-gradient(150deg,#cfd6dc,#8fb0c7 50%,#e7eaec)"></div>
  <blockquote>“. . . commissioned the new economic research report by Hollinbrook Counsel to study the industry’s . . . economic impact on states . . ”</blockquote>
  <cite>— Device Sourcing Quarterly</cite>
</article>
<article class="post" style="left:433px">
  <div class="photo" role="img" aria-label="Abstract digital medical technology visual in teal tones" style="background:linear-gradient(150deg,#0e3a46,#3c8f9c 50%,#0c2a33)"></div>
  <blockquote>“Medical Technology Industry Continues to Create High-Paying Jobs at Small Businesses Throughout Pandemic.”</blockquote>
  <cite>— Clinical Imaging Digest</cite>
</article>
<article class="post" style="left:798px">
  <div class="photo" role="img" aria-label="Sample tubes in a rack in a laboratory" style="background:linear-gradient(150deg,#8ec6d2,#d9e9ee 50%,#6e2a30)"></div>
  <blockquote>“ . . . produce more than $100 million in revenue each year, and 82 percent have fewer than 20 employees, according to Hollinbrook Counsel.”</blockquote>
  <cite>— Lone Prairie Magazine</cite>
</article>

<a class="btn abs" style="left:507px;top:4690px;width:186px;height:62px;font-size:17px">View more <span class="arr"><svg width="9" height="9" viewBox="0 0 10 10"><path d="M1 5h7M5 2l3 3-3 3" stroke="#fff" stroke-width="1.6" fill="none"/></svg></span></a>

<!-- press -->
<div class="slider-arrow" style="left:66px;top:4890px;width:38px;height:38px;background:#d9d9d9"><svg width="11" height="11" viewBox="0 0 10 10"><path d="M6.5 2L3.5 5l3 3" stroke="#fff" stroke-width="1.6" fill="none"/></svg></div>
<div class="press" style="left:130px;width:240px;font-size:36px">Ledgerline</div>
<div class="press" style="left:428px;width:188px;font-size:26px;color:#333">Northwire News</div>
<div class="press" style="left:640px;width:200px;font-size:28px">Capitol Desk</div>
<div class="press" style="left:820px;width:240px;font-size:28px">Marketvale Finance</div>
<div class="slider-arrow" style="left:1094px;top:4890px;width:38px;height:38px;background:var(--accent)"><svg width="11" height="11" viewBox="0 0 10 10"><path d="M3.5 2l3 3-3 3" stroke="#fff" stroke-width="1.6" fill="none"/></svg></div>

<!-- footer -->
<footer class="site-footer">
  <nav class="foot-nav">
    <span>HOME</span><span class="sep">|</span><span>SERVICES</span><span class="sep">|</span><span>RESEARCH</span><span class="sep">|</span><span>THE INSTITUTE</span><span class="sep">|</span><span>IN THE NEWS</span><span class="sep">|</span><span>CONTACT US</span>
  </nav>
  <div class="brand" style="left:64px;top:112px">
    <div class="brand-mark" style="border-color:var(--accent);width:78px;height:78px"></div>
    <div class="brand-name" style="color:var(--white);font-size:34px">HOLLINBROOK COUNSEL</div>
  </div>
  <div class="foot-contact" style="left:738px;top:122px"><span class="ico"><svg width="11" height="9" viewBox="0 0 11 9"><rect x=".5" y=".5" width="10" height="8" fill="none" stroke="#fff"/><path d="M.5 .5l5 4 5-4" stroke="#fff" fill="none"/></svg></span>info@hollinbrookcounsel.com</div>
  <div class="foot-contact" style="left:1004px;top:122px"><span class="ico"><svg width="10" height="10" viewBox="0 0 10 10"><path d="M2 1l2 2-1 1.5a6 6 0 0 0 2.5 2.5L7 6l2 2-1.5 1.5C4 9 1 6 .5 2.5z" fill="#fff"/></svg></span>+012 345 6789</div>
  <div class="foot-contact" style="left:780px;top:164px"><span class="ico"><svg width="9" height="11" viewBox="0 0 9 11"><path d="M4.5 11S0 6.5 0 4.5a4.5 4.5 0 0 1 9 0C9 6.5 4.5 11 4.5 11z" fill="#fff"/><circle cx="4.5" cy="4.5" r="1.6" fill="#d49a8c"/></svg></span>418 Alder Row, Suite 210, Easton, MD 21601</div>
  <div class="foot-rule"></div>
  <p class="copyright">Copyright © 2024 All Rights Reserved By Company Name</p>
</footer>

</body>
</html>
```